Design a calming beauty medical salon & spa website based in Hong Kong

We need help building an informational website for a beauty salon in Hong Kong. The local salon provides facials, massages, body and other slimming treatments in a relaxing environment. We offer some non-invasive medical treatments, such as botox. Having built the business on word of mouth, it is now time for us to launch a website to help market the business better. Website requirements:

-Must be responsive
-Use vibrant but clean colours. not too many, 1-2 colours
-Must be bilingual (switch between Chinese traditional and English)
-Our current website is host on a server, not using any particular platforms like wordpress

Pages:
1/ Homepage
2/ About us (incorporate gallery of salon photos and history of company)
3/ Promotions and latest deals (and leads them to sign up for more info, maybe pop-up small window when you click on a promotion)
4/ Treatment menus
4.1/Body treatments
4.2/ Face treatments
4.3/ Slimming treatments
5/ Showcasing products sold (no e-commerce functionality, just showing off products)
6/ Contact us (tel, address, map, opening hrs)

Footer - must haves include contact us info, privacy policy, terms & conditions, copyright blurb, join our company/employment page (with a form)

For information (comparable websites we like):
http://vostaria.com/
http://quimbel.com.hk/tc/aboutquimbel/background.php#centerenvi
Attaching a very first draft concept for this website
Attaching pictures of the beauty salon
Attaching logo

Target Market(s)

Hong Kong based, Chinese, females, 30-50+ age. 90% female clients.

Industry/Entity Type

Beauty Salon

Number of Pages Required

5+ page

Font styles to use
Sans Serif

Colors
f9d9e8
fbd3d4
fee3d5
fbe7d2
fee18a
fbf289
ffffff

Requirements
Must have
• interactive elements on website, such as scrolling banner photo headers
• incorporate photos of website salon
• connect to facebook page

```html
<!DOCTYPE html>
<html lang="en">
<head>
<meta charset="utf-8">
<title>Velora Beauty – Excellent medical beauty</title>
<link href="https://fonts.googleapis.com/css2?family=Roboto:wght@400;500&family=Great+Vibes&display=swap" rel="stylesheet">
<style>
:root{
  --page:#f8e7ef;
  --band:#f2d4d6;
  --card:#f9ebec;
  --plum:#5b1a70;
  --ink:#2b2b2b;
  --muted:#6a5a60;
  --stripe:#f3c2c8;
  --fb:#3b5a9a;
  --white:#ffffff;
}
*{box-sizing:border-box;margin:0;padding:0}
html,body{width:1200px;height:2667px;overflow:hidden}
body{background:var(--page);font-family:'Roboto',Arial,sans-serif;color:var(--ink);position:relative}
.abs{position:absolute}
.brand{font-family:'Roboto',Arial,sans-serif;font-weight:500;color:var(--plum);display:flex;align-items:center;gap:12px;white-space:nowrap}
.brand .dot{width:28px;height:28px;border-radius:50%;background:var(--plum);flex:none}

/* header */
.site-header{left:0;top:0;width:1200px;height:139px;background:var(--page)}
.header-brand{left:98px;top:52px;font-size:26px}
.contact-bar{right:98px;top:26px;display:flex;align-items:center;gap:22px;font-size:14px;color:var(--ink)}
.contact-bar .item{display:flex;align-items:center;gap:10px}
.round-icon{width:36px;height:36px;border-radius:50%;border:2px solid var(--plum);display:flex;align-items:center;justify-content:center}
.social{width:44px;height:44px;border-radius:50%;background:var(--fb)}
.lang{border:2px solid var(--plum);color:var(--plum);font-size:12px;padding:5px 10px}
.main-nav{right:98px;top:84px;display:flex;gap:40px;font-size:13.5px;text-transform:uppercase;white-space:nowrap}
.main-nav .active{color:var(--plum)}

/* hero */
.hero{left:0;top:139px;width:1200px;height:640px;background:linear-gradient(90deg,#f6ece8 0%,#f8e3dd 55%,#f5d3c8 100%);overflow:hidden}
.hero-photo{left:120px;top:0;width:460px;height:560px;background:radial-gradient(ellipse at 50% 45%,#f3dccf 0%,#ead0c3 45%,rgba(240,220,210,0) 75%)}
.hero-brand{left:650px;top:250px;font-size:50px}
.hero-brand .dot{width:44px;height:44px}
.hero-tag{left:676px;top:378px;font-size:28px;color:var(--ink)}
.hero-dots{left:1141px;top:262px;display:flex;flex-direction:column;gap:22px}
.hero-dots span{width:11px;height:11px;border-radius:50%;background:#b9a9ad}
.hero-dots span.on{background:transparent;border:1px solid #a9979b}
.hero-wave{left:0;top:660px;width:1200px;height:120px}

/* services */
.section-title{width:1200px;left:0;text-align:center;font-family:'Great Vibes',cursive;font-weight:400;font-size:54px;color:#1e1e1e}
.services-title{top:842px}
.services-intro{left:240px;top:920px;width:720px;text-align:center;font-size:13px;line-height:30px;color:var(--muted)}
.service{top:1046px;width:240px;text-align:center}
.service .photo{width:236px;height:236px;border-radius:50%;border:7px solid var(--white);margin:0 auto}
.service h3{font-weight:400;font-size:26px;margin-top:26px}
.facials{left:177px}.bodycare{left:481px}.thin{left:783px}
.facials .photo{background:linear-gradient(135deg,#e9c79a,#f3e6dc 55%,#c9a58a)}
.bodycare .photo{background:linear-gradient(160deg,#e8e2cc,#8f9a6a 55%,#4a3f34)}
.thin .photo{background:linear-gradient(150deg,#5a3628,#b57a5d 50%,#8a1f2c)}

/* contact */
.band{left:0;top:1410px;width:1200px;height:840px}
.contact-card{left:100px;top:1590px;width:1000px;height:549px;background:var(--card)}
.contact-title{top:1640px}
.info{left:151px;width:420px}
.info h4{font-weight:400;font-size:22px;margin-left:54px}
.info p{font-size:13px;line-height:26px;color:#444;margin-left:54px;margin-top:6px}
.info svg{position:absolute;left:0;top:0}
.hours{top:1764px}.hotline{top:1864px}.address{top:1962px}
.map{left:569px;top:1739px;width:478px;height:334px;background:linear-gradient(135deg,#cfe3c4 0%,#e8e2d8 40%,#efe6dc 100%)}

/* footer */
.footer-wave{left:0;top:2180px;width:1200px;height:140px}
.footer-brand{left:0;width:1200px;justify-content:center;top:2375px;font-size:34px}
.signup{left:357px;top:2459px;display:flex;gap:4px}
.signup input{width:377px;height:35px;border:none;background:var(--white);padding:0 18px;font-family:inherit;font-size:12px;color:#888}
.signup button{width:105px;height:35px;border:none;background:var(--plum);color:var(--white);font-family:inherit;font-weight:500;font-size:14px}
.footer-social{left:578px;top:2516px}
.footer-links{left:0;width:1200px;top:2578px;text-align:center;font-size:15px;color:#333}
.copyright{left:0;width:1200px;top:2614px;text-align:center;font-size:12px;color:#666}
</style>
</head>
<body>

<header class="site-header abs">
  <div class="brand header-brand abs"><span class="dot"></span>Velora Beauty</div>
  <div class="contact-bar abs">
    <div class="item"><span class="round-icon"><svg width="18" height="18" viewBox="0 0 24 24"><path d="M6.6 10.8a15 15 0 0 0 6.6 6.6l2.2-2.2c.3-.3.7-.4 1-.2 1.1.4 2.3.6 3.6.6.6 0 1 .4 1 1V20c0 .6-.4 1-1 1A17 17 0 0 1 3 4c0-.6.4-1 1-1h3.5c.6 0 1 .4 1 1 0 1.3.2 2.5.6 3.6.1.3 0 .7-.2 1z" fill="#5b1a70"/></svg></span>TEL:23458190</div>
    <div class="item"><span class="round-icon"><svg width="18" height="18" viewBox="0 0 24 24"><path d="M6.6 10.8a15 15 0 0 0 6.6 6.6l2.2-2.2c.3-.3.7-.4 1-.2 1.1.4 2.3.6 3.6.6.6 0 1 .4 1 1V20c0 .6-.4 1-1 1A17 17 0 0 1 3 4c0-.6.4-1 1-1h3.5c.6 0 1 .4 1 1 0 1.3.2 2.5.6 3.6.1.3 0 .7-.2 1z" fill="#5b1a70"/></svg></span>MOBILE : 61237745</div>
    <span class="social" aria-label="Social page"></span>
    <span class="lang">ENG ▾</span>
  </div>
  <nav class="main-nav abs">
    <span class="active">Home</span><span>About us</span><span>Promotions &amp; latest deals</span><span>Treatment ▾</span><span>Products</span><span>Contact us</span>
  </nav>
</header>

<section class="hero abs">
  <div class="hero-photo abs" role="img" aria-label="Portrait of a smiling woman with clear skin"></div>
  <div class="brand hero-brand abs"><span class="dot"></span>Velora Beauty</div>
  <div class="hero-tag abs">Excellent medical beauty</div>
  <div class="hero-dots abs"><span class="on"></span><span></span><span></span><span></span></div>
</section>
<svg class="hero-wave abs" viewBox="0 0 1200 120" preserveAspectRatio="none">
  <path d="M0 50C120 20 260 10 430 18 700 30 980 50 1200 105V120H0Z" fill="#f3c2c8"/>
  <path d="M0 62C120 32 260 24 430 32 700 44 980 64 1200 118V120H0Z" fill="#f8e7ef"/>
</svg>

<h2 class="section-title services-title abs">All for Beauty Services</h2>
<p class="services-intro abs">To take care of all aspects of the skin different needs, providing facial and body care, Customers can enjoy a more efficient and beautiful skin treatment in a relaxed and comfortable environment. Together with noble Swiss brand VeloraBeauty organic material series for home care, In order to push the quality of skin to the pinnacle.</p>

<div class="service facials abs"><div class="photo" role="img" aria-label="Woman receiving a facial mask treatment"></div><h3>Facials</h3></div>
<div class="service bodycare abs"><div class="photo" role="img" aria-label="Spa stones, towel and herbs"></div><h3>Body care</h3></div>
<div class="service thin abs"><div class="photo" role="img" aria-label="Back massage treatment"></div><h3>Thin shape</h3></div>

<svg class="band abs" viewBox="0 0 1200 840" preserveAspectRatio="none">
  <path d="M0 120C200 40 420 -10 700 30 900 60 1050 50 1200 10V840H0Z" fill="#f2d4d6"/>
</svg>

<div class="contact-card abs"></div>
<h2 class="section-title contact-title abs">Contact us</h2>

<div class="info hours abs">
  <svg width="38" height="40" viewBox="0 0 38 40" fill="none" stroke="#7a3a6a" stroke-width="2"><circle cx="19" cy="22" r="14"/><path d="M19 13v9l6 4M6 8l6-4M32 8l-6-4"/></svg>
  <h4>Opening Hours :</h4>
  <p>Monday to Friday: 10:30 am to 9:30 pm<br>Saturday and holidays: 10:30 am to 7:30 pm</p>
</div>
<div class="info hotline abs">
  <svg width="40" height="36" viewBox="0 0 40 36" fill="none" stroke="#7a3a6a" stroke-width="2"><path d="M4 12C4 6 36 6 36 12v4h-8v-4H12v4H4z"/><rect x="8" y="18" width="24" height="14" rx="2"/><circle cx="20" cy="25" r="3"/></svg>
  <h4>Inquiry Hotline :</h4>
  <p>23458190<br>61237745</p>
</div>
<div class="info address abs">
  <svg width="40" height="38" viewBox="0 0 40 38" fill="none" stroke="#7a3a6a" stroke-width="2"><path d="M3 19L20 4l17 15M8 15v20h24V15M16 35V24h8v11"/></svg>
  <h4>Address :</h4>
  <p>12th Floor, Silver Lotus Centre, 52-54 Harbour Road<br>Tsim Sha Tsui, Kowloon</p>
</div>
<div class="map abs" role="img" aria-label="Street map of Tsim Sha Tsui showing the salon location"></div>

<svg class="footer-wave abs" viewBox="0 0 1200 140" preserveAspectRatio="none">
  <path d="M0 0H1200V20C1000 100 700 120 420 100 240 90 100 90 0 110Z" fill="#f2d4d6"/>
  <path d="M0 110C100 90 240 90 420 100 700 120 1000 100 1200 20V40C1000 120 700 138 420 120 240 110 100 110 0 130Z" fill="#f3c2c8"/>
  <path d="M0 130C100 110 240 110 420 120 700 138 1000 120 1200 40V140H0Z" fill="#f8e7ef"/>
</svg>

<footer>
  <div class="brand footer-brand abs"><span class="dot"></span>Velora Beauty</div>
  <form class="signup abs"><input type="email" placeholder="Enter Email"><button type="button">JOIN US</button></form>
  <span class="social footer-social abs" aria-label="Social page"></span>
  <div class="footer-links abs">Terms and conditions &nbsp;&nbsp;/&nbsp;&nbsp; Privacy policy</div>
  <div class="copyright abs">Copyright©2018 Velora Beauty HK Ltd. All rights reserved</div>
</footer>

</body>
</html>
```